Healthcare website

We want to replace our website using joomla as the CMS. We want it to be device agnostic (gantry etc). Our business is health care our clients are people with high level spinal cord injuries ( quadriplegia / tetraplegia etc ). The site is a marketing tool primarily to potential clients and a portal for existing staff to access forms etc. It will showcase our key staff and our capability. It will also be where any new recruits apply to work with us. It must allow us to integrate our social media initiatives also. The final design must convey sophistication, high quality care and be warm and welcoming.

current web site is www.tindalehomeaid.com.au
Updates

I have made small change to the brief in that i have removed the prefered color and indicated it would be nice to see some images that symbolize change / transformation like butterflies etc. thank you

Target Market(s)

Our business is health care our clients are people with high level spinal cord injuries ( quadriplegia / tetraplegia etc ).

Industry/Entity Type

Marketing

Colors

Designer to choose colors to be used in the design.

Requirements
Must have
• The site is a marketing tool primarily to potential clients and a portal for existing staff to access forms etc. It will showcase our key staff and our capability. It will also be where any new recruits apply to work with us. It must allow us to integrate our social media initiatives also. The final design must convey sophistication, high quality care and be warm and welcoming.
Nice to have
• Would be nice to incorporate images that symbolize change and new transformations - butterflies etc.

```html
<!DOCTYPE html>
<html lang="en">
<head>
<meta charset="utf-8">
<title>Brightwing Care</title>
<link href="https://fonts.googleapis.com/css2?family=Lato:wght@300;400;700&display=swap" rel="stylesheet">
<style>
:root{
  --blue:#2b4ff0;
  --blue-dark:#1758b0;
  --text:#333;
  --orange:#f08a12;
  --footer:#232225;
  --white:#fff;
}
*{margin:0;padding:0;box-sizing:border-box}
html,body{width:720px;height:1200px;overflow:hidden}
body{font-family:'Lato',sans-serif;color:var(--text);background:var(--white);position:relative}

.site-header{position:absolute;left:0;top:0;width:720px;height:94px;background:linear-gradient(#fff,#eff0f3);box-shadow:0 2px 4px rgba(0,0,0,.25);z-index:2}
.brand{position:absolute;left:30px;top:42px;display:flex;align-items:center;gap:6px;font-size:21px;font-weight:400;color:var(--blue)}
.brand-dot{width:14px;height:14px;border-radius:50%;background:var(--blue)}
.social{position:absolute;left:546px;top:13px;display:flex;gap:4px}
.social span{width:18px;height:18px;border-radius:4px;display:block;box-shadow:inset 0 -2px 0 rgba(0,0,0,.18),0 1px 2px rgba(0,0,0,.25);position:relative;overflow:hidden}
.social span::after{content:"";position:absolute;left:0;top:0;right:0;height:9px;background:rgba(255,255,255,.28)}
.social .s1{background:#2aa4e6}.social .s2{background:#d0251c}.social .s3{background:#34538f}.social .s4{background:#1b77b0}
.main-nav{position:absolute;top:64px;left:281px;display:flex;font-size:10px;color:#333}
.main-nav a{color:inherit;text-decoration:none;margin-right:19px;position:relative}
.main-nav a.active::after{content:"";position:absolute;left:-3px;right:-3px;top:13px;height:3px;background:var(--blue)}

.hero{position:absolute;top:94px;left:0;width:720px;height:300px;overflow:hidden;
  background:
    radial-gradient(ellipse 150px 120px at 560px 170px,rgba(92,150,200,.75),rgba(92,150,200,0)),
    radial-gradient(ellipse 120px 90px at 250px 60px,rgba(214,178,150,.7),rgba(214,178,150,0)),
    radial-gradient(ellipse 110px 170px at 90px 150px,rgba(225,232,240,.9),rgba(225,232,240,0)),
    radial-gradient(ellipse 200px 90px at 600px 40px,rgba(230,236,244,.8),rgba(230,236,244,0)),
    linear-gradient(180deg,rgba(0,0,0,0) 55%,rgba(90,95,110,.35) 100%),
    linear-gradient(100deg,#b7c0cb 0%,#a9aeb6 30%,#8f98a8 55%,#8aa2bd 78%,#a9b7ad 100%)}
.hero-veil{position:absolute;inset:0;background:rgba(110,115,130,.18)}
.hero-title{position:absolute;top:76px;width:100%;text-align:center;color:#fff;font-weight:700;font-size:23px;left:4px}
.hero-sub{position:absolute;top:107px;width:100%;text-align:center;color:#fff;font-weight:300;font-size:21px;left:0}
.apply-form{position:absolute;top:175px;left:175px;display:flex;gap:17px}
.email{width:254px;height:28px;background:#ececec;border:1px solid #ccc;font-size:16px;font-weight:300;color:#999;padding-left:14px;line-height:26px}
.apply{width:102px;height:28px;background:linear-gradient(#f7a21d,var(--orange));color:#fff;font-size:17px;text-align:center;line-height:28px;box-shadow:0 2px 3px rgba(0,0,0,.3)}
.apply-note{position:absolute;top:210px;left:192px;color:#fff;font-size:11px;font-weight:400}

.welcome{position:absolute;top:394px;left:0;width:720px;height:215px;background:linear-gradient(#f8f8fa,#dfe2ea)}
.welcome h2{position:absolute;top:22px;width:100%;text-align:center;font-weight:400;font-size:16px;color:#222}
.welcome .lead{position:absolute;top:42px;width:100%;text-align:center;font-size:14px;font-weight:400;color:#222}
.feature{position:absolute;top:74px;width:186px}
.feature .icon{height:46px;display:flex;justify-content:center;align-items:center}
.feature h3{text-align:center;font-size:14px;font-weight:700;color:#333;margin-top:4px;line-height:16px}
.feature p{font-size:8px;line-height:10.5px;color:#333}

.team{position:absolute;top:609px;left:0;width:720px;height:320px}
.team h2{position:absolute;top:28px;width:100%;text-align:center;font-weight:400;font-size:18px;color:#333;left:-25px}
.member{position:absolute;top:81px;width:180px;text-align:center}
.portrait{width:108px;height:108px;border-radius:50%;margin:0 auto;box-shadow:4px 5px 6px rgba(0,0,0,.55)}
.p1{background:radial-gradient(ellipse 34px 38px at 50% 36%,#e7bfa3,rgba(231,191,163,0)),linear-gradient(#f4f1ee 0%,#f1ece7 55%,#cfe4ec 72%,#ffffff 80%,#f2f4f6 100%)}
.p2{background:radial-gradient(ellipse 32px 36px at 50% 38%,#c99677,rgba(201,150,119,0)),radial-gradient(ellipse 26px 18px at 50% 18%,#4a3c33,rgba(74,60,51,0)),linear-gradient(#f4f3f1 0%,#efecea 60%,#ffffff 78%,#e9ecef 100%)}
.p3{background:radial-gradient(ellipse 30px 36px at 50% 38%,#dcae95,rgba(220,174,149,0)),radial-gradient(ellipse 28px 16px at 50% 16%,#c9ccd0,rgba(201,204,208,0)),linear-gradient(#f5f5f5 0%,#efeeed 60%,#ffffff 74%,#2f4f8f 86%,#f0f2f4 100%)}
.member h3{margin-top:26px;font-size:18px;font-weight:700;color:var(--blue-dark)}
.member p{font-size:17px;font-weight:300;color:#333;margin-top:1px}

.testimonials{position:absolute;top:929px;left:0;width:720px;height:217px;background:linear-gradient(120deg,#5087c9 0%,#2568b9 40%,#0f55ad 100%)}
.butterfly-area{position:absolute;left:0;top:50px;width:240px;height:167px;background:radial-gradient(ellipse at 35% 55%,rgba(150,185,225,.5),rgba(80,130,200,0) 70%)}
.testimonials h2{position:absolute;top:56px;width:100%;text-align:center;left:7px;color:#fff;font-weight:400;font-size:18px}
.quotes{position:absolute;top:103px;left:83px;color:#fff;font-size:11.5px;line-height:14.5px}
.author{position:absolute;top:141px;left:547px;color:#fff;font-size:15px}

.site-footer{position:absolute;top:1146px;left:0;width:720px;height:54px;background:var(--footer);color:#8d8d8d;font-size:12px;text-align:center;padding-top:31px;padding-left:40px}
</style>
</head>
<body>
<header class="site-header">
  <div class="brand"><span>Brightwing Care</span><span class="brand-dot"></span></div>
  <div class="social" aria-label="Social links"><span class="s1"></span><span class="s2"></span><span class="s3"></span><span class="s4"></span></div>
  <nav class="main-nav">
    <a class="active" href="#">HOME</a><a href="#">ABOUT US</a><a href="#">FAQ</a><a href="#">OUR SERVICES</a><a href="#">RESOURCES</a><a href="#" style="margin-right:0">CONTACT US</a>
  </nav>
</header>

<section class="hero" role="img" aria-label="Photo of a carer walking with a client, blended with a blue butterfly on a cloudy sky">
  <div class="hero-veil"></div>
  <h1 class="hero-title">Providing in home care for people with disabilities</h1>
  <p class="hero-sub">Brightwing Care is a small team of care</p>
  <div class="apply-form"><div class="email">Your Email</div><div class="apply">Apply</div></div>
  <p class="apply-note">If you want to be a part of our Team click above to apply.</p>
</section>

<section class="welcome">
  <h2>Welcome to Brightwing Care</h2>
  <p class="lead">Quisque vestibulum gravida libero ac consectetur.</p>
  <div class="feature" style="left:67px">
    <div class="icon"><svg width="64" height="40" viewBox="0 0 64 40"><g fill="none" stroke="#2b4ff0" stroke-width="3"><circle cx="20" cy="19" r="17"/><ellipse cx="20" cy="19" rx="7" ry="17"/><line x1="3" y1="19" x2="37" y2="19"/><line x1="6" y1="10" x2="34" y2="10"/><line x1="6" y1="28" x2="34" y2="28"/><circle cx="36" cy="19" r="9" fill="#fff"/></g><line x1="43" y1="26" x2="58" y2="36" stroke="#2b4ff0" stroke-width="5" stroke-linecap="round"/></svg></div>
    <h3>Cras est sapien</h3>
    <p>vestibulum vitae euismod quis, cursus nec nibh. Proin placerat quam nec ante vestibulum, id fac ilisis neque accumsan. Mauris mollis semper sap ien et placerat. Integer</p>
  </div>
  <div class="feature" style="left:278px">
    <div class="icon"><svg width="44" height="44" viewBox="0 0 44 44"><g fill="#2b4ff0"><circle cx="15" cy="4" r="4"/><rect x="12" y="10" width="6" height="16" rx="2"/><rect x="12" y="21" width="16" height="5"/><path d="M26 21h5l6 13-4 2-5-10h-2z"/></g><path d="M9 18a12 12 0 1 0 18 14" fill="none" stroke="#2b4ff0" stroke-width="3.5"/></svg></div>
    <h3>Cras est sapien</h3>
    <p>vestibulum vitae euismod quis, cursus nec nibh. Proin placerat quam nec ante vestibulum, id fac ilisis neque accumsan. Mauris mollis semper sap ien et placerat. Integer</p>
  </div>
  <div class="feature" style="left:489px">
    <div class="icon"><svg width="44" height="46" viewBox="0 0 44 46"><g fill="#2b4ff0"><circle cx="13" cy="6" r="4.5"/><circle cx="30" cy="5" r="4.5"/><path d="M8 12h10l3 14h-4v18h-4V32h-2v12H7V26H3z"/><path d="M25 11h9l4 14-3 1v18h-4V32h-2v12h-4V24z"/></g></svg></div>
    <h3>Cras est sapien</h3>
    <p>vestibulum vitae euismod quis, cursus nec nibh. Proin placerat quam nec ante vestibulum, id fac ilisis neque accumsan. Mauris mollis semper sap ien et placerat. Integer</p>
  </div>
</section>

<section class="team">
  <h2>Our Team</h2>
  <div class="member" style="left:58px">
    <div class="portrait p1" role="img" aria-label="Portrait photo of Jane Holloway, nurse in a white coat"></div>
    <h3>Jane Holloway</h3><p>Lorem ipsum dolor si</p>
  </div>
  <div class="member" style="left:268px">
    <div class="portrait p2" role="img" aria-label="Portrait photo of Hugh Marren, doctor in a white coat"></div>
    <h3>Hugh Marren</h3><p>Lorem ipsum dolor si</p>
  </div>
  <div class="member" style="left:468px">
    <div class="portrait p3" role="img" aria-label="Portrait photo of Peter Ashby, doctor with a blue tie"></div>
    <h3>Peter Ashby</h3><p>Lorem ipsum dolor si</p>
  </div>
</section>

<section class="testimonials">
  <div class="butterfly-area" role="img" aria-label="Faint blue butterfly photo"></div>
  <h2>Testimonials</h2>
  <div class="quotes">
    <p>"Neque porro quisquam est qui dolorem ipsum quia dolor sit amet, consectetur, adipisci velit..."</p>
    <p>"No hay nadie que ame el dolor mismo, que lo busque, lo encuentre y lo quiera, simplemente porque es el dolor."</p>
  </div>
  <p class="author">Author Name</p>
</section>

<footer class="site-footer">All rights reserved 2014 Brightwing Care</footer>
</body>
</html>
```